Real Estate Agent needs business card design

We have logo designed already, want to have business card designed. Very interested in those smaller size business card as they look very trendy. Business name is called VORENDA REALTY

```html
<!DOCTYPE html>
<html lang="en">
<head>
<meta charset="utf-8">
<title>Vorenda Realty – Business Card</title>
<link href="https://fonts.googleapis.com/css2?family=Roboto:wght@400;500&display=swap" rel="stylesheet">
<style>
  :root {
    --canvas: #ece8e2;
    --tan: #c99e67;
    --tan-dark: #b88c56;
    --paper: #f3f3f3;
    --charcoal: #2e2e2e;
    --ink: #3a3a3a;
    --white: #ffffff;
    --muted: #e6e6e6;
  }
  * { box-sizing: border-box; margin: 0; padding: 0; }
  html, body { width: 1200px; height: 960px; overflow: hidden; }
  body {
    background: var(--canvas);
    font-family: "Roboto", Arial, sans-serif;
    position: relative;
  }
  .card {
    position: absolute;
    left: 320px;
    width: 600px;
    height: 342px;
    border-radius: 16px;
    overflow: hidden;
    box-shadow: 0 2px 6px rgba(0,0,0,0.18);
  }
  /* Front */
  .card-front {
    top: 108px;
    background: var(--tan);
  }
  .front-brand {
    position: absolute;
    top: 128px; left: 0; right: 0;
    display: flex; align-items: center; justify-content: center; gap: 16px;
    color: var(--white);
    font-size: 38px;
    font-weight: 500;
    letter-spacing: 4px;
  }
  .brand-square {
    width: 22px; height: 22px;
    background: var(--white);
  }
  .front-web {
    position: absolute;
    top: 300px; left: 0; right: 0;
    text-align: center;
    color: var(--white);
    font-size: 13px;
    letter-spacing: 8px;
  }
  /* Back */
  .card-back {
    top: 493px;
    background: var(--paper);
  }
  .back-band {
    position: absolute; top: 0; left: 0; right: 0;
    height: 31px;
    background: var(--tan);
  }
  .band-notch {
    position: absolute; top: 30px; left: 283px;
  }
  .back-brand {
    position: absolute;
    top: 90px; left: 0; right: 0;
    display: flex; align-items: center; justify-content: center; gap: 14px;
    color: var(--ink);
    font-size: 32px;
    font-weight: 400;
    letter-spacing: 3px;
  }
  .back-brand .brand-square { background: var(--tan); width: 18px; height: 18px; }
  .contact-panel {
    position: absolute; left: 0; right: 0; bottom: 0;
    height: 140px;
    background: var(--charcoal);
    color: var(--white);
  }
  .contact-list {
    position: absolute; top: 20px; left: 41px;
    list-style: none;
    font-size: 14px;
    line-height: 19.3px;
  }
  .contact-list li { display: flex; align-items: center; gap: 10px; }
  .contact-list svg { width: 12px; height: 12px; fill: var(--white); flex: none; }
  .person {
    position: absolute; top: 24px; right: 34px;
    text-align: right;
  }
  .person-name { font-size: 19px; font-weight: 500; line-height: 22px; }
  .person-role { font-size: 14px; font-weight: 500; color: var(--muted); margin-top: 2px; }
  .person-address { font-size: 14px; line-height: 19px; margin-top: 17px; }
</style>
</head>
<body>

  <section class="card card-front" aria-label="Card front">
    <div class="front-brand"><span class="brand-square"></span><span>VORENDA REALTY</span></div>
    <p class="front-web">www.vorenda.com</p>
  </section>

  <section class="card card-back" aria-label="Card back">
    <div class="back-band"></div>
    <svg class="band-notch" width="34" height="14" viewBox="0 0 34 14"><polygon points="0,0 34,0 17,14" fill="var(--tan)"/></svg>

    <div class="back-brand"><span class="brand-square"></span><span>VORENDA REALTY</span></div>

    <div class="contact-panel">
      <ul class="contact-list">
        <li><svg viewBox="0 0 12 12"><path d="M2.4 0.6l2 0 .8 2.6-1.3 1c.7 1.5 1.8 2.6 3.3 3.3l1-1.3 2.6.8v2c0 .7-.6 1.2-1.3 1.1C4.6 9.7 1.9 7 1.5 2c-.1-.8.4-1.4.9-1.4z"/></svg>555 210 4471</li>
        <li><svg viewBox="0 0 12 12"><path d="M3 0h6a1 1 0 0 1 1 1v10a1 1 0 0 1-1 1H3a1 1 0 0 1-1-1V1a1 1 0 0 1 1-1zm.4 1.5v7.5h5.2V1.5zM6 9.8a.7.7 0 1 0 0 1.4.7.7 0 0 0 0-1.4z"/></svg>555 318 9064</li>
        <li><svg viewBox="0 0 12 12"><path d="M3 0h6v3H3zM1 4h10a1 1 0 0 1 1 1v4h-2v3H2V9H0V5a1 1 0 0 1 1-1zm2 4v3h6V8z"/></svg>555 742 1980</li>
        <li><svg viewBox="0 0 12 12"><path d="M0 2.5h12v.6L6 7 0 3.1zM0 4.4l6 3.8 6-3.8V10H0z"/></svg>info@vorenda.com</li>
        <li><svg viewBox="0 0 12 12"><path d="M6 0a6 6 0 1 0 0 12A6 6 0 0 0 6 0zm-1 2.2c.6.5.2 1.2-.4 1.5-.8.4-.4 1.2.4 1.3.9.1 1.4.8 1 1.6-.3.7.3 1.3.1 2.1-.2.6-.9.6-1.2 0-.5-.8-1.2-1.6-2.2-2.3-.7-.6-.9-1.6-.5-2.6.6-1.3 2.1-2.1 2.8-1.6zm3.6 1.4c.8.3 1.4 1.3 1.3 2.3-.4-.2-.9-.1-1.2.3-.4-.5-.5-1.4-.1-2.6z"/></svg>www.vorenda.com</li>
      </ul>

      <div class="person">
        <p class="person-name">DANA WHITLOW</p>
        <p class="person-role">CEO/FOUNDER</p>
        <p class="person-address">4120 Larkspur Court<br>Fairbanks, Alaska 99701</p>
      </div>
    </div>
  </section>

</body>
</html>
```